Plastic Aesthetic and Reconstructive Surgery

I need a double sided luxurius Business Card, with a minimal, modern design focused on my job.
Besides my Name, Surname and contact information, the use of my initials (M and T) in free style combination as a logo will help.
In the one side all data written in English.
In the other side written in Greek if possible.
Please feel free to use the letter type and size you prefer.
Please use icons type and size and orientation you like.
The Name, Surname, occupation and the initials can be UV spotted.
You can use also in the background a texture or something that will make the card luxurious.
I would prefer pal colors.
Each side can have different colors or even better they can be reversed or inverted
As I have said you can use the wet sand color, light brown, dark brown, gold, light gold, white
Updates

Need extra days to review

i am waiting for some new ideas and some modifications from the designers. I need a couple of days extention of the period for the designers to post their modifications.

Target Market(s)

Patients who need a reconstructive intervention or surgery. Also people, mainly women, that they need aesthetic or cosmetic interventions to face or body

Contact Information for Business Card

Name and surname, occupation, member of an organization , mobile telephone number, Mail, Facebook and Instagram accounts

Font styles to use
Script
Other font styles liked:
• Gabriola

Colors
FFC000
F8CF3A
FAE287
FDF2CF
FEFAEE

Requirements
Must have
• A free combination of my initials (M and T) as a logo
Nice to have
• Fade out with the background colors, UV spotted of the name, initials logo
Should not have
• Address

```html
<!DOCTYPE html>
<html lang="en">
<head>
<meta charset="utf-8">
<title>Business Card – Dr. Marcus Tavridis</title>
<link rel="stylesheet" href="https://fonts.googleapis.com/css2?family=Poppins:wght@500&family=EB+Garamond:ital,wght@0,400;1,400&family=Roboto:wght@400&display=swap">
<style>
  :root {
    --page-bg: #ffffff;
    --sand: #a58a74;
    --sand-shadow: #98806b;
    --sand-mark: #6f5642;
    --sand-name: #8a6f5a;
    --card-white: #ffffff;
    --ink: #2b2b2b;
    --copper: #c4845a;
    --tan: #dcb592;
    --ghost: #efefef;
    --rule: #c9ccd3;
  }
  * { margin: 0; padding: 0; box-sizing: border-box; }
  html, body {
    width: 1200px; height: 2400px; overflow: hidden;
    background: var(--page-bg);
  }
  .card {
    position: absolute; left: 160px;
    width: 880px; height: 502px; overflow: hidden;
    box-shadow: 2px 3px 6px rgba(0,0,0,0.35);
  }
  .card--front { top: 660px; background: var(--sand); }
  .card--back  { top: 1240px; background: var(--card-white); }

  .card__decor { position: absolute; inset: 0; }

  .brand-mark {
    position: absolute; display: flex; align-items: center; justify-content: center;
    border-radius: 50%;
    font-family: "EB Garamond", serif; font-weight: 400;
  }
  .card--front .brand-mark {
    left: 590px; top: 30px; width: 200px; height: 200px;
    border: 3px solid var(--sand-mark); color: var(--sand-mark); font-size: 34px;
  }
  .card--back .brand-mark {
    left: 662px; top: 28px; width: 128px; height: 128px;
    border: 2px solid var(--tan); color: var(--tan); font-size: 23px;
  }

  .doctor-name {
    position: absolute; text-align: center;
    font-family: "Poppins", sans-serif; font-weight: 500;
    white-space: nowrap;
  }
  .card--front .doctor-name {
    left: 480px; top: 243px; width: 420px;
    font-size: 22px; letter-spacing: 5px; color: var(--sand-name);
  }
  .card--back .doctor-name {
    left: 516px; top: 171px; width: 420px;
    font-size: 18px; letter-spacing: 4px; color: var(--tan);
  }

  .specialty-front {
    position: absolute; left: 480px; top: 306px; width: 420px; text-align: center;
    font-family: "EB Garamond", serif; font-size: 16px; color: #ffffff; white-space: nowrap;
  }

  .profile { position: absolute; left: 55px; top: 226px; font-family: "EB Garamond", serif; }
  .profile__name { font-size: 21px; color: var(--copper); letter-spacing: 0.5px; }
  .profile__line { font-size: 18px; color: var(--ink); line-height: 28px; }

  .divider {
    position: absolute; left: 55px; top: 360px; width: 790px; height: 1px;
    background: var(--rule);
  }

  .contact {
    position: absolute; display: flex; align-items: center; gap: 10px;
    font-family: "Roboto", sans-serif; color: var(--ink); font-size: 20px;
  }
  .contact--phone { left: 55px; top: 386px; }
  .contact--mail  { left: 55px; top: 428px; }
  .contact--social { left: 755px; top: 432px; font-size: 15px; gap: 8px; }
  .contact svg { display: block; }
  .dot { width: 18px; height: 18px; border-radius: 50%; background: var(--tan); }
  .contact--social .dot { width: 15px; height: 15px; }
</style>
</head>
<body>

<section class="card card--front" aria-label="Business card, front">
  <svg class="card__decor" width="880" height="502" aria-hidden="true">
    <circle cx="180" cy="262" r="250" fill="none" stroke="var(--sand-shadow)" stroke-width="6"/>
  </svg>
  <div class="brand-mark">Tavridis</div>
  <p class="doctor-name">DR. MARCUS TAVRIDIS</p>
  <p class="specialty-front">Πλαστική Επανορθωτική και Αισθητική Χειρουργική</p>
</section>

<section class="card card--back" aria-label="Business card, back">
  <svg class="card__decor" width="880" height="502" aria-hidden="true">
    <circle cx="735" cy="215" r="215" fill="none" stroke="var(--ghost)" stroke-width="6"/>
  </svg>
  <div class="brand-mark">Tavridis</div>
  <p class="doctor-name">DR. MARCUS TAVRIDIS</p>

  <div class="profile">
    <p class="profile__name">ΜΑΡΚΟΣ ΤΑΒΡΙΔΗΣ, MD, MSC</p>
    <p class="profile__line">Πλαστική Επανορθωτική και Αισθητική Χειρουργική</p>
    <p class="profile__line">Μέλος Σ.Α.Χ.Ε.Τ.Ο</p>
  </div>

  <div class="divider"></div>

  <p class="contact contact--phone">
    <svg width="20" height="20" viewBox="0 0 24 24" aria-hidden="true">
      <path fill="var(--tan)" d="M6.6 10.8c1.4 2.8 3.8 5.1 6.6 6.6l2.2-2.2c.3-.3.7-.4 1-.2 1.1.4 2.3.6 3.6.6.6 0 1 .4 1 1V20c0 .6-.4 1-1 1C10.6 21 3 13.4 3 4c0-.6.4-1 1-1h3.5c.6 0 1 .4 1 1 0 1.2.2 2.4.6 3.6.1.3 0 .7-.2 1l-2.3 2.2z"/>
    </svg>
    <span class="dot" aria-hidden="true"></span>
    <span>+30 690 123 4567</span>
  </p>
  <p class="contact contact--mail">
    <svg width="20" height="14" viewBox="0 0 20 14" aria-hidden="true">
      <rect x="0.5" y="0.5" width="19" height="13" fill="var(--tan)"/>
      <path d="M1 1l9 7 9-7" fill="none" stroke="#fff" stroke-width="1.3"/>
    </svg>
    <span>m.tavridis@example.com</span>
  </p>
  <p class="contact contact--social">
    <span class="dot" aria-hidden="true"></span>
    <span>/drmtav/</span>
  </p>
</section>

</body>
</html>
```